The hardcover "Star Chronicle" (large size, Quarto 4º, 12 × 9 1/2 in, 30.5 × 24.15 cm) in German language as follows:

STERNENCHRONIK (title)
der herausragendsten Unternehmer und Manager Deutschlands 2013 (subtitle 1)
BERLIN UND BRANDENBURG (subtitle 2, smaller than subtitle 1)

Morvalto (logo, WMF file attached)
Updates

Reason: The solutions are rather too childish and pre-made styles... is there anyone who can make it better? - a professional-looking business book (encyclopedia style, should have no color-pictures, no author's name, logo smaller due to the large size book)

Target Market(s)

business community

Requirements
Must have
• encyclopedia style large size book
must look professional and expensive

Nice to have
• - gold-color hardcover, or some gold-color elements
- some simple and decent graphic element (e.g. an ancient column, or some other architectural detail), if any
Should not have
• no color-pictures
no author's name

```html
<!DOCTYPE html>
<html lang="de">
<head>
<meta charset="utf-8">
<title>Sternenchronik – Buchumschlag</title>
<link rel="stylesheet" href="https://fonts.googleapis.com/css2?family=Cinzel:wght@500;600&family=Montserrat:wght@600&display=swap">
<style>
  :root {
    --page-bg: #ececec;
    --cover-bg: #ffffff;
    --ink: #111111;
    --gold-deep: #5a3a12;
    --gold-mid: #9a6a2a;
    --gold-light: #e6c27a;
    --gold-pale: #f6e7a8;
  }
  html, body {
    margin: 0;
    width: 1000px;
    height: 1200px;
    overflow: hidden;
    background: var(--page-bg);
  }
  .book-cover {
    position: absolute;
    left: 140px;
    top: 32px;
    width: 752px;
    height: 1133px;
    background: var(--cover-bg);
  }
  .cover-art {
    display: block;
    width: 100%;
    height: 100%;
  }
  .title-word {
    font-family: "Montserrat", "Century Gothic", sans-serif;
    font-weight: 600;
  }
  .subtitle-main {
    font-family: "Cinzel", "Trajan Pro", serif;
    font-weight: 600;
    font-size: 30px;
    fill: var(--ink);
  }
  .subtitle-region {
    font-family: "Cinzel", "Trajan Pro", serif;
    font-weight: 500;
    font-size: 23px;
    fill: var(--ink);
  }
  .rule {
    stroke: var(--ink);
    stroke-width: 3;
  }
</style>
</head>
<body>
  <main class="book-cover">
    <svg class="cover-art" viewBox="0 0 752 1133" xmlns="http://www.w3.org/2000/svg" aria-labelledby="cover-title">
      <title id="cover-title">Sternenchronik der herausragendsten Unternehmer und Manager Deutschlands 2013 – Berlin und Brandenburg</title>
      <defs>
        <linearGradient id="gold-foil" x1="0" y1="0" x2="1" y2="1">
          <stop offset="0" stop-color="var(--gold-deep)"/>
          <stop offset="0.3" stop-color="var(--gold-mid)"/>
          <stop offset="0.48" stop-color="var(--gold-light)"/>
          <stop offset="0.55" stop-color="var(--gold-pale)"/>
          <stop offset="0.7" stop-color="var(--gold-mid)"/>
          <stop offset="1" stop-color="var(--gold-deep)"/>
        </linearGradient>
      </defs>

      <g class="title-block" fill="url(#gold-foil)">
        <text class="title-word" x="38" y="478" font-size="128" textLength="677" lengthAdjust="spacingAndGlyphs">STERNEN</text>
        <text class="title-word" x="38" y="678" font-size="160" textLength="677" lengthAdjust="spacingAndGlyphs">CHRONIK</text>
      </g>

      <line class="rule" x1="185" y1="710" x2="612" y2="710"/>
      <text class="subtitle-main" x="65" y="746" textLength="653" lengthAdjust="spacingAndGlyphs">Der herausragendsten Unternehmer und</text>
      <text class="subtitle-main" x="148" y="780" textLength="437" lengthAdjust="spacingAndGlyphs">Manager Deutschlands 2013</text>
      <line class="rule" x1="185" y1="792" x2="612" y2="792"/>
      <text class="subtitle-region" x="235" y="821" textLength="342" lengthAdjust="spacingAndGlyphs">BERLIN UND BRANDENBURG</text>
    </svg>
  </main>
</body>
</html>
```